Custon Magnetic Case Packaging Design

1. Please follow the updated PPT to each detaili.
Updates

Target Market(s)

sports card / trading card / collectors

Requirements
Must have
• Subtle Sports Themes, but clean / modern. Nothing childish.
Nice to have
• All instructions followed
Should not have
• too many random colors

```html
<!DOCTYPE html>
<html lang="en">
<head>
<meta charset="utf-8">
<title>CaseVault Magnetic Case Packaging</title>
<link rel="stylesheet" href="https://fonts.googleapis.com/css2?family=Barlow+Condensed:wght@600;700&family=Barlow:wght@700&display=swap">
<style>
  :root {
    --backdrop: #d9d9d9;
    --card-dark: #262626;
    --card-dark-2: #333333;
    --gold: #e9a93a;
    --panel-light: #f2f2f2;
    --panel-shade: #dedede;
    --case-red: #b3191e;
    --label-white: #f4f4f4;
  }
  html, body {
    margin: 0;
    padding: 0;
    width: 1200px;
    height: 750px;
    overflow: hidden;
    background: var(--backdrop);
  }
  .stage {
    display: block;
    width: 1200px;
    height: 750px;
  }
  .brand-name {
    font-family: "Barlow Condensed", sans-serif;
    font-weight: 700;
    font-size: 30px;
    fill: var(--label-white);
    letter-spacing: 1px;
  }
  .tagline {
    font-family: "Barlow", sans-serif;
    font-weight: 700;
    font-size: 9px;
    fill: var(--label-white);
    letter-spacing: 3.2px;
  }
  .feature-label {
    font-family: "Barlow Condensed", sans-serif;
    font-weight: 600;
    font-size: 8.5px;
    fill: var(--label-white);
  }
  .gold-line { fill: none; stroke: var(--gold); stroke-width: 2; }
  .gold-thin { fill: none; stroke: var(--gold); stroke-width: 1; }
  .icon-stroke { fill: none; stroke: var(--label-white); stroke-width: 2.5; stroke-linecap: round; }
  .icon-fill { fill: var(--label-white); }
</style>
</head>
<body>
<svg class="stage" viewBox="0 0 1200 750" xmlns="http://www.w3.org/2000/svg">
  <defs>
    <linearGradient id="cardShade" x1="0" x2="1" y1="0" y2="0">
      <stop offset="0" stop-color="var(--card-dark-2)"/>
      <stop offset="1" stop-color="var(--card-dark)"/>
    </linearGradient>
    <linearGradient id="caseWindow" x1="0" x2="1" y1="0" y2="0">
      <stop offset="0" stop-color="var(--case-red)"/>
      <stop offset="0.06" stop-color="var(--case-red)"/>
      <stop offset="0.07" stop-color="#111"/>
      <stop offset="0.09" stop-color="#f4f4f2"/>
      <stop offset="0.91" stop-color="#ebebe8"/>
      <stop offset="0.93" stop-color="#111"/>
      <stop offset="0.94" stop-color="var(--case-red)"/>
      <stop offset="1" stop-color="var(--case-red)"/>
    </linearGradient>
    <linearGradient id="sidePanel" x1="0" x2="1" y1="0" y2="0">
      <stop offset="0" stop-color="var(--panel-shade)"/>
      <stop offset="1" stop-color="var(--panel-light)"/>
    </linearGradient>
  </defs>

  <!-- card body -->
  <path class="card" d="M410 80 Q410 50 440 50 L760 50 Q790 50 790 80 L790 710 L410 710 Z" fill="url(#cardShade)"/>

  <!-- hang hole -->
  <path class="hang-hole" d="M566 82 H590 A10 10 0 0 1 610 82 H634 A8 8 0 0 1 634 98 H566 A8 8 0 0 1 566 82 Z" fill="var(--panel-light)"/>

  <!-- header arc and side rules -->
  <path class="gold-line" d="M438 50 A168 120 0 0 0 762 50"/>
  <line class="gold-line" x1="468" y1="140" x2="468" y2="228"/>
  <line class="gold-thin" x1="482" y1="148" x2="482" y2="232"/>
  <line class="gold-line" x1="732" y1="140" x2="732" y2="242"/>
  <line class="gold-thin" x1="718" y1="148" x2="718" y2="240"/>

  <!-- shoulder bands -->
  <path class="gold-line" d="M410 200 Q470 215 530 242"/>
  <path class="gold-thin" d="M410 210 Q470 225 530 250"/>
  <path class="gold-line" d="M790 210 Q730 225 672 250"/>
  <path class="gold-thin" d="M790 220 Q730 235 672 258"/>

  <!-- product window -->
  <rect class="product-window" x="470" y="232" width="262" height="316" fill="url(#caseWindow)" role="img" aria-label="Red magnetic card case visible through the clear window"/>

  <!-- tagline band -->
  <rect class="tagline-band" x="465" y="548" width="272" height="50" fill="var(--card-dark)"/>
  <line class="gold-line" x1="465" y1="548" x2="737" y2="548"/>
  <text class="tagline" x="601" y="577" text-anchor="middle">PROTECT YOURSLABS IN STYLE</text>

  <!-- side panels -->
  <path class="side-panel" d="M410 240 H450 Q465 240 465 258 V562 H410 Z" fill="url(#sidePanel)" role="img" aria-label="Light dotted texture panel"/>
  <path class="gold-line" d="M410 240 H450 Q465 240 465 258 V562 H410"/>
  <path class="side-panel" d="M790 262 H752 Q737 262 737 280 V600 Q737 615 752 618 L790 622 Z" fill="url(#sidePanel)" role="img" aria-label="Light dotted texture panel"/>
  <path class="gold-line" d="M790 262 H752 Q737 262 737 280 V600 Q737 615 752 618 L790 622"/>

  <!-- logo tab -->
  <path class="logo-tab" d="M522 160 Q600 178 680 160 L670 275 Q668 288 655 288 H545 Q532 288 530 275 Z" fill="var(--card-dark)"/>
  <path class="gold-line" d="M522 160 Q600 178 680 160 L670 275 Q668 288 655 288 H545 Q532 288 530 275 Z"/>
  <rect class="brand-mark" x="588" y="206" width="24" height="24" fill="var(--label-white)"/>
  <text class="brand-name" x="600" y="268" text-anchor="middle">CASEVAULT</text>

  <!-- lower arcs -->
  <path class="gold-line" d="M410 612 Q600 560 790 662"/>
  <path class="gold-thin" d="M410 622 Q600 572 790 672"/>
  <line class="gold-thin" x1="432" y1="562" x2="432" y2="604"/>
  <line class="gold-thin" x1="768" y1="622" x2="768" y2="652"/>

  <!-- feature icons -->
  <g class="feature feature-crack">
    <path class="icon-stroke" d="M477 628 L472 640 L479 648 L476 656"/>
    <text class="feature-label" x="476" y="672" text-anchor="middle">CRACK</text>
    <text class="feature-label" x="476" y="681" text-anchor="middle">RESISTANT</text>
  </g>
  <g class="feature feature-stack">
    <rect class="icon-fill" x="527" y="632" width="18" height="4"/>
    <rect class="icon-fill" x="527" y="639" width="18" height="4"/>
    <rect class="icon-fill" x="527" y="646" width="18" height="4"/>
    <text class="feature-label" x="536" y="677" text-anchor="middle">STACKABLE</text>
  </g>
  <g class="feature feature-colors">
    <circle cx="592" cy="636" r="2.5" fill="#e0457b"/>
    <circle cx="600" cy="636" r="2.5" fill="#e94b3c"/>
    <circle cx="608" cy="636" r="2.5" fill="#f39c12"/>
    <circle cx="592" cy="644" r="2.5" fill="#f1c40f"/>
    <circle cx="600" cy="644" r="2.5" fill="#c7d12a"/>
    <circle cx="608" cy="644" r="2.5" fill="#27ae60"/>
    <circle cx="592" cy="652" r="2.5" fill="#16a085"/>
    <circle cx="600" cy="652" r="2.5" fill="#2980b9"/>
    <circle cx="608" cy="652" r="2.5" fill="#8e44ad"/>
    <text class="feature-label" x="600" y="670" text-anchor="middle">VARIOUS</text>
    <text class="feature-label" x="600" y="679" text-anchor="middle">COLORS</text>
  </g>
  <g class="feature feature-uv">
    <path class="icon-stroke" d="M657 638 L664 646 L672 636"/>
    <line class="icon-stroke" x1="656" y1="652" x2="674" y2="652"/>
    <text class="feature-label" x="674" y="633" text-anchor="middle">UV</text>
    <text class="feature-label" x="665" y="667" text-anchor="middle">UV</text>
    <text class="feature-label" x="665" y="676" text-anchor="middle">PROTECTION</text>
  </g>
  <g class="feature feature-lock">
    <path class="icon-stroke" d="M725 648 V642 A5 5 0 0 1 735 642 V648"/>
    <rect class="icon-fill" x="722" y="647" width="16" height="12" rx="2"/>
    <text class="feature-label" x="730" y="673" text-anchor="middle">SAFTEY</text>
    <text class="feature-label" x="730" y="682" text-anchor="middle">LOCK</text>
  </g>
</svg>
</body>
</html>
```